Need Help having my business card stand out

I am the owner of Pine Ridge Canine Coaching and would like for my business cards to stand out. I have been trying to keep designing them myself but I can't get what I have in my head on the card. I will try my best to post templates that I like for inspirations. I want something unique but elegant. I don't want in to look cartoony or cheesy. It needs to pop in a pet shop but also in a coffee shop or gym.

Target Market(s)

Dog owners, Married ,No young kids Jr High school kids and up (maybe kids on the way) Executives, Stay at home moms/wives, Small business owners

Industry/Entity Type

Dog Training

Contact Information for Business Card

Trevor Holloway, 555-304-7162, info@pineridgecanine.example, www.pineridgecanine.example

Colors

Designer to choose colors to be used in the design.

Requirements
Must have
• my logo
Should not have
• Cursive lettering

```html
<!DOCTYPE html>
<html lang="en">
<head>
<meta charset="utf-8">
<title>Pine Ridge Canine Coaching — Business Card</title>
<link href="https://fonts.googleapis.com/css2?family=Jost:wght@300;400;500;700&display=swap" rel="stylesheet">
<style>
  :root {
    --red-light: #f2806e;
    --red-mid: #e8412c;
    --red-deep: #dc1f0e;
    --white: #ffffff;
    --ink: #3a3a3a;
    --mark-grey: #5a5a5a;
    --backdrop: #ebe7e3;
  }
  html, body {
    margin: 0;
    padding: 0;
    width: 1200px;
    height: 960px;
    overflow: hidden;
    background: var(--backdrop);
    font-family: "Jost", sans-serif;
  }
  .canvas {
    position: relative;
    width: 1200px;
    height: 960px;
  }
  .card {
    position: absolute;
    left: 250px;
    width: 700px;
    height: 400px;
    overflow: hidden;
    box-shadow: 0 6px 18px rgba(0,0,0,0.18);
  }
  .card--front { top: 50px; background: linear-gradient(200deg, var(--red-light) 0%, var(--red-mid) 45%, var(--red-deep) 100%); }
  .card--back { top: 510px; background: var(--white); }

  .front__band {
    position: absolute;
    left: 0; right: 0; bottom: 0;
    height: 76px;
    background: var(--white);
    display: flex;
    align-items: center;
  }
  .front__website {
    margin-left: 360px;
    font-size: 19px;
    font-weight: 400;
    letter-spacing: 0.5px;
    color: var(--ink);
    white-space: nowrap;
  }
  .front__mark {
    position: absolute;
    left: 0; top: 176px;
    width: 215px;
    height: 130px;
    background: var(--white);
    display: flex;
    align-items: center;
    justify-content: center;
  }
  .brand-name {
    font-family: "Jost", sans-serif;
    font-weight: 500;
    color: var(--mark-grey);
    text-align: center;
    line-height: 1.15;
  }
  .front__mark .brand-name { font-size: 20px; }
  .front__name {
    position: absolute;
    left: 292px; top: 100px;
    margin: 0;
    font-size: 46px;
    font-weight: 300;
    letter-spacing: 1px;
    line-height: 1.1;
    color: var(--white);
    white-space: nowrap;
  }
  .front__icons {
    position: absolute;
    left: 292px; top: 196px;
    width: 96px; height: 82px;
    background: var(--white);
  }
  .front__contact {
    position: absolute;
    left: 404px; top: 198px;
    color: var(--white);
    white-space: nowrap;
  }
  .front__phone { margin: 0; font-size: 23px; font-weight: 700; letter-spacing: 0.5px; line-height: 1.2; }
  .front__email { margin: 12px 0 0; font-size: 18px; font-weight: 300; letter-spacing: 0.3px; line-height: 1.2; }

  .back__shape { position: absolute; inset: 0; }
  .back__mark {
    position: absolute;
    left: 300px; top: 190px;
    width: 290px;
    display: flex;
    align-items: center;
    justify-content: center;
  }
  .back__mark .brand-name { font-size: 34px; }
</style>
</head>
<body>
<main class="canvas">

  <section class="card card--front" aria-label="Business card front">
    <div class="front__mark">
      <span class="brand-name">Pine Ridge<br>Canine Coaching</span>
    </div>
    <h1 class="front__name">Trevor Holloway</h1>
    <svg class="front__icons" viewBox="0 0 96 82" aria-hidden="true">
      <path d="M36 16 c-3 2 -3 6 0 10 c3 4 7 7 11 8 c3 1 5 -1 6 -3 l-3 -3 l-4 2 c-3 -1 -6 -4 -7 -7 l2 -4 z" fill="none" stroke="#555" stroke-width="1.6"/>
      <rect x="46" y="50" width="26" height="17" fill="none" stroke="#555" stroke-width="1.6"/>
      <path d="M46 50 l13 10 l13 -10" fill="none" stroke="#555" stroke-width="1.6"/>
      <path d="M28 56 h12 M32 61 h8 M30 66 h10" stroke="#555" stroke-width="1.6"/>
    </svg>
    <div class="front__contact">
      <p class="front__phone">555-304-7162</p>
      <p class="front__email">info@pineridgecanine.example</p>
    </div>
    <div class="front__band">
      <span class="front__website">www.pineridgecanine.example</span>
    </div>
  </section>

  <section class="card card--back" aria-label="Business card back">
    <svg class="back__shape" viewBox="0 0 700 400" aria-hidden="true">
      <defs>
        <linearGradient id="backRed" x1="1" y1="0" x2="0" y2="1">
          <stop offset="0" stop-color="#f2806e"/>
          <stop offset="0.45" stop-color="#e8412c"/>
          <stop offset="1" stop-color="#dc1f0e"/>
        </linearGradient>
      </defs>
      <rect width="700" height="400" fill="url(#backRed)"/>
      <circle cx="440" cy="290" r="225" fill="#fff"/>
      <rect x="560" y="125" width="140" height="275" fill="#fff"/>
      <rect x="0" y="322" width="700" height="78" fill="#fff"/>
    </svg>
    <div class="back__mark">
      <span class="brand-name">Pine Ridge<br>Canine Coaching</span>
    </div>
  </section>

</main>
</body>
</html>
```